Re-Design an adult education portal

I need support to re-design an adult education portal. Currently the customer has an incomplete website which should be prepared in a new format.
I have the idea how to realize, but I have no clue how to design it. The hard thing is to have a "beautiful" website with available logo and main color. I hope you can support me.

Name of Website: tovelu (tovelu.example)
Content: adult eduction for adult in safety at work, mountain climbing, dog school. various courses in different areas. But on old webpage is hard to find the different possibilities.
main color: Ral 6011 (green) -> #6C7C59
logo: you see on top of website the logo (2 dogs and a mountain with a colour gradient).

new website: for new webpage I decided to have a navigation for each section of education. In the main area I would like to have some pictures to give an idea what content is behind. At the moment it looks terrible, so I decided to use you as support for me to make the webpage prettier :). And maybe you have an better idea how to make it great. -> current state of new web page: https://tovelu.brisk-host.example/

Target Market(s)

adult eduction for adult in safety at work, mountain climbing, dog school

Number of Pages Required

1 page

Font styles to use
Serif
Sans Serif

Requirements
Must have
• As main color is set "Ral 6011" (green) -> #6C7C59

```html
<!DOCTYPE html>
<html lang="en">
<head>
<meta charset="utf-8">
<title>tovelu – Training and courses</title>
<link rel="stylesheet" href="https://fonts.googleapis.com/css2?family=Poppins:wght@400;500;600&display=swap">
<style>
  :root {
    --green: #6c7c59;
    --sand: #dcdcbc;
    --ink: #111111;
    --white: #ffffff;
    --dot: #c9c9c9;
  }
  * { margin: 0; padding: 0; box-sizing: border-box; }
  html, body { width: 1200px; height: 2165px; overflow: hidden; background: var(--white); }
  body { position: relative; font-family: 'Poppins', sans-serif; color: var(--ink); }
  .abs { position: absolute; }

  .brand { left: 134px; top: 24px; display: flex; align-items: center; gap: 8px; font-size: 20px; font-weight: 500; color: var(--ink); }
  .brand-mark { width: 14px; height: 14px; border-radius: 50%; background: var(--green); }

  .hero-photo { left: 533px; top: 0; width: 667px; height: 853px;
    background:
      radial-gradient(ellipse 30% 40% at 88% 45%, rgba(200,80,40,0.55), transparent 70%),
      radial-gradient(ellipse 22% 30% at 45% 52%, rgba(170,200,60,0.45), transparent 70%),
      radial-gradient(ellipse 45% 25% at 60% 88%, rgba(40,50,60,0.45), transparent 70%),
      radial-gradient(ellipse 50% 22% at 55% 28%, rgba(210,150,80,0.5), transparent 70%),
      linear-gradient(165deg, #4b4a3a 0%, #6d6a52 18%, #cbbd9c 42%, #d9cfb4 62%, #c4b598 82%, #a89476 100%); }
  .menu { left: 1032px; top: 24px; width: 30px; height: 20px; }
  .block { background: var(--green); }
  .block-hero-top { left: 635px; top: 190px; width: 147px; height: 130px; }
  .block-hero-left { left: 34px; top: 523px; width: 312px; height: 156px; }
  .hero-card { left: 80px; top: 227px; width: 666px; height: 403px; background: var(--sand); padding: 50px 54px; }
  .hero-card h1 { font-size: 42px; font-weight: 600; line-height: 54px; letter-spacing: -0.3px; }
  .hero-card p { margin-top: 22px; font-size: 20px; line-height: 30px; width: 420px; }
  .btn { display: inline-block; margin-top: 22px; width: 213px; height: 53px; line-height: 53px; text-align: center; background: var(--green); color: var(--white); font-size: 20px; }

  .block-right { left: 1067px; top: 986px; width: 133px; height: 84px; }
  .block-left { left: 0; top: 1736px; width: 134px; height: 84px; }

  .course { width: 453px; height: 453px; display: flex; align-items: center; justify-content: center; }
  .course::after { content: ""; position: absolute; inset: 0; background: rgba(0,0,0,0.18); }
  .course span { position: relative; z-index: 1; color: var(--white); font-size: 20px; text-align: center; line-height: 25px; }
  .course .tag { background: var(--green); width: 213px; height: 53px; line-height: 53px; }
  .c-forklift { left: 134px; top: 937px;
    background:
      radial-gradient(ellipse 55% 30% at 60% 72%, rgba(214,50,40,0.95), transparent 75%),
      radial-gradient(ellipse 40% 40% at 55% 30%, rgba(40,40,40,0.6), transparent 75%),
      linear-gradient(180deg, #e6e6e6 0%, #bdbdbd 25%, #3a3a3a 55%, #c8342c 75%, #2b2b2b 100%); }
  .c-forklift span { margin-left: -40px; }
  .c-dog { left: 613px; top: 937px;
    background:
      radial-gradient(ellipse 45% 25% at 60% 28%, rgba(110,120,70,0.7), transparent 75%),
      radial-gradient(ellipse 30% 25% at 30% 45%, rgba(90,60,40,0.6), transparent 75%),
      linear-gradient(180deg, #2c2a22 0%, #4b4636 35%, #5f6a3c 70%, #7b8a4e 100%); }
  .c-dog::after { background: rgba(0,0,0,0.3); }
  .c-mountain { left: 134px; top: 1417px;
    background:
      radial-gradient(ellipse 30% 30% at 42% 40%, rgba(150,40,50,0.55), transparent 75%),
      radial-gradient(ellipse 25% 18% at 38% 18%, rgba(240,240,240,0.7), transparent 75%),
      linear-gradient(180deg, #e3e6e8 0%, #9aa0a2 30%, #77786c 60%, #8d8c76 85%, #b1b09a 100%); }
  .c-platform { left: 613px; top: 1417px;
    background:
      radial-gradient(ellipse 30% 12% at 65% 55%, rgba(230,110,50,0.6), transparent 75%),
      radial-gradient(ellipse 28% 35% at 15% 60%, rgba(90,75,55,0.7), transparent 75%),
      linear-gradient(180deg, #5b8fd6 0%, #a9c2df 25%, #6f7360 48%, #7a7a70 62%, #b3b3ae 100%); }
  .c-platform span { margin-top: -28px; }

  .arrow { width: 40px; height: 30px; }
  .arrow-prev { left: 67px; top: 1388px; }
  .arrow-next { left: 1093px; top: 1388px; }

  .dots { left: 555px; top: 1895px; display: flex; align-items: center; gap: 10px; }
  .dots i { display: block; width: 13px; height: 13px; border-radius: 50%; background: var(--dot); }
  .dots i.active { width: 19px; height: 19px; background: var(--green); }
  .dots i:last-child { background: #dedede; }

  .site-footer { left: 0; top: 1998px; width: 1200px; height: 167px; background: var(--sand); text-align: center; padding-top: 47px; }
  .site-footer h2 { font-size: 20px; font-weight: 400; line-height: 26px; }
  .site-footer address { font-style: normal; margin-top: 13px; font-size: 9.5px; line-height: 15px; }
</style>
</head>
<body>
  <header>
    <div class="abs brand"><span class="brand-mark"></span>tovelu.example</div>
    <div class="abs hero-photo" role="img" aria-label="Construction workers in hard hats and high-visibility jackets on a building site"></div>
    <svg class="abs menu" viewBox="0 0 30 20" aria-label="Menu"><g stroke="#fff" stroke-width="2"><line x1="0" y1="2" x2="30" y2="2"/><line x1="0" y1="10" x2="30" y2="10"/><line x1="0" y1="18" x2="30" y2="18"/></g></svg>
  </header>

  <section>
    <div class="abs block block-hero-top"></div>
    <div class="abs block block-hero-left"></div>
    <div class="abs hero-card">
      <h1>Your training and<br>course partner</h1>
      <p>We offer training tailored to your needs, target-oriented and tailored to your skills and knowledge.</p>
      <a class="btn">Start Now</a>
    </div>
  </section>

  <section>
    <div class="abs block block-right"></div>
    <div class="abs block block-left"></div>
    <div class="abs course c-forklift" role="img" aria-label="Red forklift truck"><span>Forklift Course</span></div>
    <div class="abs course c-dog" role="img" aria-label="Dogs resting by a mossy log in a forest"><span class="tag">Dog School</span></div>
    <div class="abs course c-mountain" role="img" aria-label="Climber with helmet on a mountain ridge"><span>Mountain Training</span></div>
    <div class="abs course c-platform" role="img" aria-label="Aerial work platform extended outdoors"><span>Aerial Work<br>Platform</span></div>

    <svg class="abs arrow arrow-prev" viewBox="0 0 40 30" aria-label="Previous"><rect x="1" y="1" width="38" height="28" rx="3" fill="none" stroke="#111" stroke-width="2"/><path d="M28 15H13M19 9l-6 6 6 6" fill="none" stroke="#111" stroke-width="2"/></svg>
    <svg class="abs arrow arrow-next" viewBox="0 0 40 30" aria-label="Next"><rect x="1" y="1" width="38" height="28" rx="3" fill="none" stroke="#111" stroke-width="2"/><path d="M12 15h15M21 9l6 6-6 6" fill="none" stroke="#111" stroke-width="2"/></svg>

    <div class="abs dots"><i></i><i class="active"></i><i></i><i></i></div>
  </section>

  <footer class="abs site-footer">
    <h2>Tovelu GmbH</h2>
    <address>Lindenweg 27, CH-3900 Brig<br>Phone: +41 79 000 12 34<br>Email: info@tovelu.example</address>
  </footer>
</body>
</html>
```